Property investment company needs a letterhead design!

We are a new residential and commercial property investment company. Name of the company is Morvesta Group, LLC. We have a new logo and now we need letterhead! We prefer to have a professional and upscale appearance. We don't have any fixed requirements, so be creative! Thank you for considering this project. We are so excited to see what happens!

Target Market(s)

Professional

Industry/Entity Type

Real Estate Development

```html
<!DOCTYPE html>
<html lang="en">
<head>
<meta charset="utf-8">
<title>Morvesta Group, LLC — Letterhead</title>
<link rel="stylesheet" href="https://fonts.googleapis.com/css2?family=Lato:wght@400;700;900&family=Great+Vibes&display=swap">
<style>
  :root {
    --backdrop: #e4e4e4;
    --paper: #f7f7f7;
    --navy: #0f2440;
    --sky: #1ea5e2;
    --ink: #4a4a4a;
    --ink-soft: #6b6b6b;
    --rule: #c9c9c9;
  }
  * { box-sizing: border-box; margin: 0; padding: 0; }
  html, body { width: 1200px; height: 900px; overflow: hidden; }
  body {
    background: var(--backdrop);
    font-family: "Lato", Arial, sans-serif;
    color: var(--ink);
    display: flex;
    justify-content: center;
    align-items: center;
    gap: 24px;
  }
  .sheet {
    position: relative;
    width: 553px;
    height: 780px;
    background: linear-gradient(135deg, #fbfbfb 0%, #f1f1f1 100%);
    box-shadow: 0 2px 6px rgba(0,0,0,0.18);
  }
  .sheet__bar {
    position: absolute; top: 0; left: 0; width: 100%; height: 7px;
  }
  .brand {
    position: absolute; top: 34px; left: 46px;
    display: flex; align-items: center; gap: 8px;
  }
  .brand__dot {
    width: 22px; height: 22px; border-radius: 50%; background: var(--navy);
  }
  .brand__name {
    font-weight: 900; font-size: 19px; letter-spacing: 0.5px; color: var(--navy);
  }
  .letter {
    position: absolute; top: 168px; left: 59px; width: 437px;
    font-size: 8.6px; line-height: 13px; color: var(--ink-soft);
  }
  .letter__date { margin-bottom: 13px; }
  .letter__recipient { margin-bottom: 25px; }
  .letter__recipient strong { color: #222; font-weight: 700; }
  .letter__greeting { margin-bottom: 13px; }
  .letter p.body { text-align: justify; margin-bottom: 13px; }
  .letter__closing { margin-top: 35px; }
  .letter__signature {
    font-family: "Great Vibes", cursive; font-size: 21px; color: #222;
    margin-top: 4px; margin-left: 5px;
  }
  .footer {
    position: absolute; left: 45px; right: 45px; top: 716px;
    border-top: 1px solid var(--rule);
    padding-top: 11px;
    display: flex; justify-content: space-between;
    font-size: 9.4px; line-height: 11.5px; color: var(--ink-soft);
  }
  .footer__contact li { list-style: none; display: flex; align-items: center; gap: 5px; }
  .footer__contact svg { width: 7px; height: 7px; fill: var(--navy); }
  .footer__address { text-align: right; font-style: normal; }
</style>
</head>
<body>

<article class="sheet">
  <svg class="sheet__bar" viewBox="0 0 553 7" preserveAspectRatio="none" aria-hidden="true">
    <rect width="553" height="7" fill="var(--navy)"/>
    <polygon points="0,0 156,0 162,7 0,7" fill="var(--sky)"/>
  </svg>
  <div class="brand"><span class="brand__dot"></span><span class="brand__name">MORVESTA</span></div>

  <div class="letter">
    <p class="letter__date">01 January 2050</p>
    <p class="letter__recipient"><strong>Company (Pvt) Ltd.</strong><br>PO Box 3355 Mainville St<br>Sample City Country 3355</p>
    <p class="letter__greeting">Dear Laura Whitcombe,</p>
    <p class="body">Lorem ipsum dolor sit amet, consectetuer adipiscing elit, sed diam nonummy nibh euismod tincidunt ut laoreet dolore magna aliquam erat volutpat. Ut wisi enim ad minim veniam, quis nostrud exerci tation ullamcorper suscipit lobortis nisl ut aliquip ex ea commodo consequat. Duis dolore te feugait nulla facilisi. Nam liber tempor cum soluta nobis eleifend option congue nihil imperdiet doming id quod mazim placerat facer possim assum. Lorem ipsum dolor sit amet, consectetuer adipiscing elit, sed diam nonummy nibh euismod tincidunt ut laoreet dolore magna aliquam erat volutpat. Ut wisi enim ad minim veniam, quis nostrud exerci tation ullamcorper suscipit lobortis nisl ut aliquip ex ea commodo consequat.</p>
    <p class="body">Consectetuer adipiscing elit, sed diam nonummy nibh euismod tincidunt ut laoreet dolore magna aliquam erat volutpat. Ut wisi enim ad minim veniam, quis nostrud exerci tation ullamcorper suscipit lobortis nisl ut aliquip ex ea commodo consequat. Consectetuer adipiscing elit, sed diam nonummy nibh euismod tincidunt ut laoreet dolore magna aliquam erat volutpat. Ut wisi enim ad minim veniam, quis nostrud exerci tation ullamcorper suscipit lobortis nisl ut aliquip ex ea commodo consequat.</p>
    <p class="body">Consectetuer adipiscing elit, sed diam nonummy nibh euismod tincidunt ut laoreet dolore magna aliquam erat volutpat. Ut wisi enim ad minim veniam, quis nostrud exerci tation ullamcorper suscipit lobortis nisl ut aliquip ex ea commodo consequat. Consectetuer adipiscing elit, sed diam nonummy nibh euismod tincidunt ut laoreet dolore magna aliquam erat volutpat. Ut wisi enim ad minim veniam, quis nostrud exerci tation ullamcorper suscipit lobortis nisl ut aliquip ex ea commodo consequat.</p>
    <p class="letter__closing">Sincerely Yours</p>
    <p class="letter__signature">Daniel Roy Ashford</p>
  </div>

  <footer class="footer">
    <ul class="footer__contact">
      <li><svg viewBox="0 0 10 10" aria-hidden="true"><path d="M2 0l2 2-1 2 3 3 2-1 2 2-2 2C4 10 0 6 0 2z"/></svg>(555) 214-7380</li>
      <li><svg viewBox="0 0 10 10" aria-hidden="true"><path d="M0 2h10v6H0zM0 2l5 3 5-3"/></svg>MorvestaLLC@gmail.com</li>
      <li><svg viewBox="0 0 10 10" aria-hidden="true"><circle cx="5" cy="5" r="5"/></svg>www.MorvestaLLC.com</li>
    </ul>
    <address class="footer__address">Morvesta Group, LLC<br>418 N. Alder Way<br>Linden Falls, MI 40000</address>
  </footer>
</article>

<article class="sheet">
  <svg class="sheet__bar" viewBox="0 0 553 7" preserveAspectRatio="none" aria-hidden="true">
    <rect width="553" height="7" fill="var(--navy)"/>
    <polygon points="0,0 156,0 162,7 0,7" fill="var(--sky)"/>
  </svg>
  <div class="brand"><span class="brand__dot"></span><span class="brand__name">MORVESTA</span></div>

  <footer class="footer">
    <ul class="footer__contact">
      <li><svg viewBox="0 0 10 10" aria-hidden="true"><path d="M2 0l2 2-1 2 3 3 2-1 2 2-2 2C4 10 0 6 0 2z"/></svg>(555) 214-7380</li>
      <li><svg viewBox="0 0 10 10" aria-hidden="true"><path d="M0 2h10v6H0zM0 2l5 3 5-3"/></svg>MorvestaLLC@gmail.com</li>
      <li><svg viewBox="0 0 10 10" aria-hidden="true"><circle cx="5" cy="5" r="5"/></svg>www.MorvestaLLC.com</li>
    </ul>
    <address class="footer__address">Morvesta Group, LLC<br>418 N. Alder Way<br>Linden Falls, MI 40000</address>
  </footer>
</article>

</body>
</html>
```